Software Platform User Guide (Manual)

We need a user manual template for our online e-learning platform, Lectern, which allows users to create their own online courses.

We’re looking for a template for a few pages, including a cover, back page, table of contents, and pages for text-only (or bullet points), and text & images (screenshots). We would like to be able to add new pages and adjust textual content ourselves. Lorem ipsum is totally cool as placeholder text. The name of the product is Lectern, but the company name is Mutual Cadence, so we would like the cover and back cover to say “Mutual Cadence" and "Lectern".

We have uploaded a few files to give you a sense of our color scheme and logo. You can also check out our website at mcvista.example for an idea of our aesthetic sensibility. The design should be simple and elegant, and (being a user manual) clarity is king. We use Avenir and Elizabeth as or primary fonts. We have also uploaded some sample screen shots from Lectern. You can use those screenshots to help direct your work, but note that the interface design is changing soon; i.e., you should emphasize the Mutual Cadence brand aesthetic more so than the Lectern user interface design.

Target Market(s)

Businesses and nonprofits looking to implement our platform. Many buyers are female, but the people reading the manual are typically male.

Industry/Entity Type

It Company

Requirements
Must have
• The final product must be a template that will work in Microsoft Word, PowerPoint, or Apple Keynote/Pages. It's fine to send PDFs for previews. Note we need the final product in ONE of the above choices (Word, Powerpoint, Keynote, or Pages), not ALL.

You must make use of the MC logo and fonts on every page. Note that the tag line, "shortest distance between two points of view" in one version of the logo does note have to be included.

We need clear delineation between headers, sub-headers, and bullets, as well as a great looking cover, table of contents and back page.

Please Note: Please disregard the OLVA logo on any screenshots. These were mockups for a client. Please don't use the OLVA name or logo.

```html
<!DOCTYPE html>
<html lang="en">
<head>
<meta charset="utf-8">
<title>Lectern User Guide — Contents</title>
<link rel="stylesheet" href="https://fonts.googleapis.com/css2?family=Bodoni+Moda:wght@500&family=Nunito+Sans:wght@400;700;800&display=swap">
<style>
  :root {
    --slate: #5f6670;
    --slate-line: rgba(255, 255, 255, 0.32);
    --lime: #bccb2c;
    --periwinkle: #6b8fd2;
    --rule: #b9c9ea;
    --ink: #1d1d1f;
    --paper: #ffffff;
  }
  * { box-sizing: border-box; margin: 0; padding: 0; }
  html, body { width: 1200px; height: 848px; overflow: hidden; background: var(--paper); }
  .spread { position: relative; width: 1200px; height: 848px; font-family: "Nunito Sans", Arial, sans-serif; color: var(--ink); }

  .facing-panel { position: absolute; left: 0; top: 0; width: 596px; height: 848px; background: var(--slate); }
  .facing-panel svg { display: block; }

  .contents-page { position: absolute; left: 596px; top: 0; width: 604px; height: 848px; }
  .page-title {
    position: absolute; left: 148px; top: 28px;
    font-family: "Bodoni Moda", "Times New Roman", serif; font-weight: 500;
    font-size: 44px; line-height: 1; color: var(--lime); letter-spacing: 0.2px;
  }
  .intro {
    position: absolute; left: 147px; top: 128px; width: 380px;
    font-size: 11px; line-height: 16.3px;
  }
  .toc { position: absolute; left: 40px; top: 186px; width: 500px; list-style: none; }
  .toc-entry { display: grid; grid-template-columns: 51px 380px; column-gap: 56px; margin-bottom: 8px; }
  .toc-page { text-align: right; font-weight: 800; font-size: 18px; line-height: 24px; color: var(--lime); }
  .toc-heading { font-weight: 800; font-size: 18.5px; line-height: 24px; color: var(--periwinkle); }
  .toc-summary { font-size: 11px; line-height: 16.3px; }

  .footer-rule { position: absolute; left: 61px; top: 765px; width: 474px; height: 1px; background: var(--rule); }
  .brand {
    position: absolute; left: 140px; top: 800px;
    font-family: "Nunito Sans", Arial, sans-serif; font-weight: 700;
    font-size: 13px; color: var(--periwinkle);
  }
</style>
</head>
<body>
<div class="spread">
  <aside class="facing-panel" aria-hidden="true">
    <svg width="596" height="848" viewBox="0 0 596 848">
      <g stroke="var(--slate-line)" stroke-width="1">
        <line x1="177.5" y1="0" x2="177.5" y2="762"/><line x1="197.5" y1="0" x2="197.5" y2="762"/>
        <line x1="217.5" y1="0" x2="217.5" y2="762"/><line x1="237.5" y1="0" x2="237.5" y2="762"/>
        <line x1="257.5" y1="0" x2="257.5" y2="762"/><line x1="277.5" y1="0" x2="277.5" y2="762"/>
        <line x1="297.5" y1="0" x2="297.5" y2="762"/><line x1="317.5" y1="0" x2="317.5" y2="762"/>
        <line x1="337.5" y1="0" x2="337.5" y2="762"/><line x1="357.5" y1="0" x2="357.5" y2="762"/>
        <line x1="377.5" y1="0" x2="377.5" y2="762"/><line x1="397.5" y1="0" x2="397.5" y2="762"/>
        <line x1="417.5" y1="0" x2="417.5" y2="762"/><line x1="437.5" y1="0" x2="437.5" y2="762"/>
        <line x1="457.5" y1="0" x2="457.5" y2="762"/><line x1="477.5" y1="0" x2="477.5" y2="762"/>
        <line x1="497.5" y1="0" x2="497.5" y2="762"/><line x1="517.5" y1="0" x2="517.5" y2="762"/>
        <line x1="537.5" y1="0" x2="537.5" y2="762"/><line x1="557.5" y1="0" x2="557.5" y2="762"/>
        <line x1="577.5" y1="0" x2="577.5" y2="762"/>
        <line x1="0" y1="803.5" x2="596" y2="803.5"/>
        <line x1="0" y1="822.5" x2="596" y2="822.5"/>
      </g>
    </svg>
  </aside>

  <main class="contents-page">
    <h1 class="page-title">Contents</h1>
    <p class="intro">Qui blaborem quam Duat enduci delibust autem harit quunt es ipsapis et occatat ecaerib eribus quatus estioneseque pore latusam, tor alitias nonsend issimodicil ipsum faciati aut perro con niendam utae.</p>

    <ol class="toc">
      <li class="toc-entry">
        <span class="toc-page">4</span>
        <div><h2 class="toc-heading">Pid eos sint harumqui</h2>
        <p class="toc-summary">Xerchicium aperunti omnis sam ex essequam ea plaborum explignate.</p></div>
      </li>
      <li class="toc-entry">
        <span class="toc-page">8</span>
        <div><h2 class="toc-heading">Hue simped molorest</h2>
        <p class="toc-summary">Et et la vendam, occumquat volupta epeliqu aeperepuda is expellende sam quam ut molut alit fugit.</p></div>
      </li>
      <li class="toc-entry">
        <span class="toc-page">12</span>
        <div><h2 class="toc-heading">Et et la vendam occumquat</h2>
        <p class="toc-summary">Renis necerit aut harum fugaor accume nobis aut destt id eos et ullabor epelest endignate recte porepelitate minimus sam, to tem faciist ab imagnih iliameni reribea suntores sinustrum as consed misim acc.</p></div>
      </li>
      <li class="toc-entry">
        <span class="toc-page">26</span>
        <div><h2 class="toc-heading">Pos sint haqui</h2>
        <p class="toc-summary">Xerchicium aperunti omnis sam ex essequam ea plaborum.</p></div>
      </li>
      <li class="toc-entry">
        <span class="toc-page">49</span>
        <div><h2 class="toc-heading">Hiwn molorest</h2>
        <p class="toc-summary">Et et la vendam, occumquat volupta epeliqu aeperepuda is expellende sam quam ut molut alit fugit.</p></div>
      </li>
      <li class="toc-entry">
        <span class="toc-page">90</span>
        <div><h2 class="toc-heading">Tem fugit untu aturitiun</h2>
        <p class="toc-summary">Renis necerit aut harum fugaor accume nobis aut destt id eos et ullabor epelest endignate recte porepelitate minimus sam, to tem faciist ab imagnih iliameni reribea suntores sinustrum as consed misim acc.</p></div>
      </li>
    </ol>

    <div class="footer-rule"></div>
    <p class="brand">Mutual Cadence</p>
  </main>
</div>
</body>
</html>
```